Business card and stationary for a consultant firm
Sharp Compass
Professional
Renske Hoorneman
Zwaluwlaan 38
Curaçao
Renskehoorneman@postvlek.com
Zwaluwlaan38

```html
<!DOCTYPE html>
<html lang="en">
<head>
<meta charset="utf-8">
<title>Sharp Compass – Business Card</title>
<link rel="stylesheet" href="https://fonts.googleapis.com/css2?family=Libre+Baskerville:wght@700&family=Cormorant+SC:wght@500;600&display=swap">
<style>
  :root {
    --page-bg: #ecebe7;
    --card-bg: #ffffff;
    --ink: #1d1d1b;
    --accent-orange: #e07b1f;
    --olive-light: #c9c24a;
    --olive-dark: #8d8a22;
    --muted: #5a5a55;
    --card-shadow: rgba(0, 0, 0, 0.16);
  }
  * { box-sizing: border-box; margin: 0; padding: 0; }
  html, body {
    width: 1200px; height: 629px; overflow: hidden;
    background: var(--page-bg);
  }
  .canvas { position: relative; width: 1200px; height: 629px; }
  .card {
    position: absolute; top: 166px;
    width: 520px; height: 297px;
    background: var(--card-bg);
    box-shadow: 0 6px 18px var(--card-shadow);
    overflow: hidden;
  }
  .card--front { left: 50px; }
  .card--back { left: 630px; }

  .brand {
    display: flex; align-items: center; gap: 12px;
    white-space: nowrap;
  }
  .brand__mark {
    flex: none;
    width: 30px; height: 30px; border-radius: 50%;
    background: var(--olive-light);
  }
  .brand__name {
    font-family: "Libre Baskerville", Georgia, serif;
    font-weight: 700; color: var(--ink);
    letter-spacing: -0.3px;
  }
  .card--front .brand {
    position: absolute; left: 50%; top: 50%;
    transform: translate(-50%, -50%);
  }
  .card--front .brand__mark { width: 36px; height: 36px; }
  .card--front .brand__name { font-size: 28px; }

  .card--back .brand { position: absolute; left: 38px; top: 62px; }
  .card--back .brand__name { font-size: 21px; }

  .contact-list {
    position: absolute; left: 304px; top: 44px;
    list-style: none;
    font-family: "Cormorant SC", Georgia, serif;
    font-weight: 600; font-size: 12px; color: var(--muted);
    white-space: nowrap;
  }
  .contact-list li {
    display: flex; align-items: center; gap: 7px;
    height: 19px;
  }
  .contact-list svg { width: 9px; height: 9px; flex: none; }

  .person {
    position: absolute; left: 56px; top: 138px;
    font-family: "Cormorant SC", Georgia, serif;
    white-space: nowrap;
  }
  .person__name {
    font-size: 14px; font-weight: 600; color: var(--accent-orange);
    letter-spacing: 0.6px;
  }
  .person__address {
    margin-top: 10px;
    font-size: 11px; font-weight: 500; color: var(--muted);
    letter-spacing: 0.5px;
  }

  .footer-band {
    position: absolute; left: 0; bottom: 0;
    width: 520px; height: 56px;
    background: linear-gradient(90deg, var(--olive-dark), var(--olive-light) 55%, #a9a431);
  }
</style>
</head>
<body>
<main class="canvas">

  <section class="card card--front" aria-label="Card front">
    <div class="brand">
      <span class="brand__mark"></span>
      <span class="brand__name">Sharp Compass</span>
    </div>
  </section>

  <section class="card card--back" aria-label="Card back">
    <div class="brand">
      <span class="brand__mark"></span>
      <span class="brand__name">Sharp Compass</span>
    </div>

    <ul class="contact-list">
      <li>
        <svg viewBox="0 0 10 10"><rect width="10" height="10" rx="2" fill="#e07b1f"/><path d="M3 2.5 L4.3 4 L3.8 4.6 Q4.6 5.8 5.4 6.2 L6 5.7 L7.5 7 L6.8 7.8 Q4 7.5 2.2 3.2 Z" fill="#fff"/></svg>
        +599 9 555 0142
      </li>
      <li>
        <svg viewBox="0 0 10 10"><rect width="10" height="10" rx="2" fill="#e07b1f"/><rect x="2" y="3" width="6" height="4.2" fill="none" stroke="#fff" stroke-width="0.9"/><path d="M2 3 L5 5.4 L8 3" fill="none" stroke="#fff" stroke-width="0.9"/></svg>
        Renskehoorneman@postvlek.com
      </li>
      <li>
        <svg viewBox="0 0 10 10"><rect width="10" height="10" rx="2" fill="#e07b1f"/><circle cx="5" cy="5" r="2.6" fill="none" stroke="#fff" stroke-width="0.9"/><path d="M2.4 5 H7.6 M5 2.4 V7.6" stroke="#fff" stroke-width="0.7"/></svg>
        www.zwaluwlaan38.com
      </li>
    </ul>

    <div class="person">
      <p class="person__name">Renske Hoorneman</p>
      <p class="person__address">Zwaluwlaan 38 Curaçao</p>
    </div>

    <div class="footer-band" role="img" aria-label="Decorative olive wave band along the bottom edge"></div>
  </section>

</main>
</body>
</html>
```